website design + images

We need a very appealing website design, layout and images for a sales analytics and sales productivity services company based in San Ramon, California. We need a good design for the home page and a template for all other pages (total 2 designs), and images for all inner pages (center column/banner images, and right hand top corner small images). There are about 18 inner pages.
Updates

Our existing website is www.corvexa.com
Our corporate colours are the ones that are there on the website. The logo is also shown. We will be changing the tagline to "accelerating revenue" or equivalent of that.

Please use the document "website for corvexa - template v2.doc" that I just uploaded for any reference to the content, navigation and wireframes. A few more clarifications are provided mainly for the link "Solutions".

Hemant Loravi

Hi,
We just uploaded ver 4 of the website template. There is more elaboration provided around the sublinks / sections for Solutions. Pls review and do get back if you need any clarifications.

Rgds
Hemant Loravi

Hi all,
We have so far received a few good designs. The designs are more or less on the right track. I would like to urge all of you to use the content and navigation provided in the document attached to our brief "website for corvexa - template v4.doc".  Please DO NOT use the content in our existing website www.corvexa.com . That is very old. We mentioned it only for reference to colour theme and broad details.

We have totally 13 sections in Solutions pages. They may be designed as a tree of links - first level sublinks - second level sublinks or links - first level sublinks and the remaining as sections within the first level sublinks pages. The page design would remain the same for all inner pages except careers. But after finalizing the design for the inner page, we will need images for the different inner pages.

Rgds
Hemant Loravi

Hi,
Thank you all for participation and very good designs. We are quite happy with what we have seen. We have now shortlisted about 4 vendors and sending invididual feedback to them for further improvement. We will be finalizing by Monday or Tuesday.  To the vendors who do not get feedback from us, thank you very much for participation. We may still do business in future for some of our other needs. 
The following are the process steps / expectations going forward, 
1. Feedback to the shortlisted designers and inviting improvements.
2. Review of the improved designs and further shortlist & feedback or direct finalization.
3. The design should be in 1024*768
2. Number of page designs = 2 (home page, inner page).
4. Home page design: instead of delivery model and customers, show one link "Why Us".
4. Solutions page design:  We will be needing an image in center column of solutions page that in a nutshell gives all the different types of solutions we provide. The entire set of solutions is in our attached document website for corvexa - template v4 and I am just uploading v5 with more description on sublinks.
5. After selection, we will be needing images for all the solution pages (total 12 pages under solutions + one solutions page), 1 image for Why Us?, 1 for Careers, and 3 for company (about us/ team, core values, ...) = total 18

Rgds
Hemant Loravi

Target Market(s)

We are a sales analytics and sales productivity services company. We help B2B companies with: sales planning; sales operations and sales measurement. The characteristics of our customers are:
- B2B medium enterprises (USD 100M- USD 2B in revenue) in the US
- Primary target verticals are: high-tech, engineering and professional services firms
- Our primary target customers titles are VP of Sales or VP of marketing; we could be selling to the CEO at companies with revenues below $200M

Industry/Entity Type

Consulting

Requirements
Must have
• - Clean, uncluttered design
• - Easy navigation; minimum clicks
Nice to have
• We have already built a content management system and wireframes for this site. To the extent possible, it would be great to leverage the wireframe structure we built, provided you don’t have to compromise on the look and feel and navigation of the site. Below is what we currently have as banner sizes and resolutions are:
• Home page banner size: 950 * 250’
• All pages – center top - image size: 558 * 160
• All pages – right hand top image – 175*135’

```html
<!DOCTYPE html>
<html lang="en">
<head>
<meta charset="utf-8">
<title>Corvexa – Solutions</title>
<link href="https://fonts.googleapis.com/css2?family=Arimo:ital,wght@0,400;0,700;1,400&display=swap" rel="stylesheet">
<style>
  :root {
    --page-bg: #ececec;
    --panel-bg: #f4f4f4;
    --white: #ffffff;
    --brand-blue: #0b5ca8;
    --link-blue: #0a4f94;
    --text-gray: #7a7a7a;
    --nav-gray: #8a8a8a;
    --rule-blue: #1f6cb4;
    --frame-gray: #e4e4e4;
  }
  * { margin: 0; padding: 0; box-sizing: border-box; }
  html, body { width: 1200px; height: 900px; overflow: hidden; }
  body {
    position: relative;
    background: var(--page-bg);
    font-family: "Arimo", Arial, sans-serif;
    color: var(--text-gray);
  }
  .backdrop {
    position: absolute; left: 10px; top: 0; width: 1180px; height: 122px;
    background: var(--panel-bg);
  }
  .header {
    position: absolute; left: 48px; top: 0; width: 1115px; height: 124px;
    background: var(--white);
  }
  .utility-links {
    position: absolute; right: 42px; top: 16px;
    font-size: 14px; color: var(--text-gray);
  }
  .brand { position: absolute; left: 29px; top: 58px; }
  .brand-row { display: flex; align-items: center; gap: 10px; }
  .brand-dot {
    width: 18px; height: 18px; border-radius: 50%;
    background: var(--brand-blue);
  }
  .brand-name {
    font-size: 28px; font-weight: 700; color: var(--brand-blue); line-height: 1;
  }
  .brand-tagline {
    margin-top: 6px; font-size: 14px; color: var(--text-gray); line-height: 1;
  }
  .main-nav { position: absolute; top: 99px; left: 0; width: 100%; }
  .main-nav a {
    position: absolute; font-size: 13px; font-weight: 700;
    color: var(--nav-gray); text-decoration: none; white-space: nowrap;
  }
  .main-nav a.is-active { color: var(--brand-blue); }

  .banner {
    position: absolute; left: 48px; top: 124px; width: 1113px; height: 158px;
    box-shadow: 0 3px 5px rgba(0,0,0,.25);
    overflow: hidden;
  }
  .banner-photo {
    position: absolute; inset: 0;
    background: linear-gradient(90deg, #0c5aa6 0%, #1c6fbb 30%, #5d9ad3 55%, #a9c9e6 75%, #c9dcec 100%);
  }
  .banner-title {
    position: absolute; left: 31px; top: 87px;
    font-size: 28px; font-weight: 700; color: var(--white);
  }

  .card {
    position: absolute; background: var(--white);
    box-shadow: 0 2px 5px rgba(0,0,0,.28);
  }
  .content-card { left: 52px; top: 302px; width: 786px; height: 524px; }
  .links-card { left: 860px; top: 302px; width: 303px; height: 524px; }
  .section-heading {
    position: absolute; top: 18px;
    font-size: 14px; font-weight: 700; color: var(--brand-blue);
    border-bottom: 1px solid var(--rule-blue); padding-bottom: 3px;
  }
  .content-card .section-heading { left: 27px; width: 738px; }
  .links-card .section-heading { left: 13px; width: 273px; }
  .section-heading .more { position: absolute; right: 2px; top: -1px; font-size: 16px; }

  .intro-copy {
    position: absolute; left: 27px; top: 60px; width: 462px;
    font-size: 14.3px; line-height: 21px;
  }
  .intro-copy p + p { margin-top: 21px; }
  .intro-copy strong { color: #777; }

  .photo-frame {
    position: absolute; left: 514px; top: 65px; width: 246px; height: 246px;
    background: var(--frame-gray);
    box-shadow: inset 0 0 4px rgba(0,0,0,.15);
  }
  .photo-top, .photo-bottom { position: absolute; left: 13px; width: 223px; }
  .photo-top {
    top: 17px; height: 116px;
    background: linear-gradient(135deg, #d9dcd2 0%, #b7bdae 50%, #7e8a7f 100%);
  }
  .photo-bottom {
    top: 134px; height: 94px;
    background: linear-gradient(90deg, #bfd2d6 0%, #e6ebe8 45%, #eee3d4 100%);
  }

  .related-links { position: absolute; left: 13px; top: 60px; list-style: none; }
  .related-links li { height: 42px; }
  .related-links a {
    font-size: 14px; font-weight: 700; color: var(--link-blue); text-decoration: none;
  }

  .footer {
    position: absolute; left: 52px; top: 847px; width: 1113px; height: 41px;
    background: var(--white); box-shadow: 0 2px 5px rgba(0,0,0,.28);
  }
  .footer-note {
    position: absolute; right: 38px; top: 14px;
    font-size: 13px; font-style: italic; color: var(--text-gray);
  }
</style>
</head>
<body>
  <div class="backdrop"></div>

  <header class="header">
    <div class="utility-links">Sitemap | Sign in / Register | Contact us</div>
    <div class="brand">
      <div class="brand-row">
        <span class="brand-dot"></span>
        <span class="brand-name">Corvexa</span>
      </div>
      <div class="brand-tagline">accelerating revenue</div>
    </div>
    <nav class="main-nav">
      <a class="is-active" style="left:329px">HOME</a>
      <a style="left:479px">SOLUTIONS</a>
      <a style="left:666px">WHY US?</a>
      <a style="left:832px">COMPANY</a>
      <a style="left:1008px">CAREERS</a>
    </nav>
  </header>

  <section class="banner">
    <div class="banner-photo" role="img" aria-label="Businesswoman with a laptop seated on a mountain top under a wide blue sky"></div>
    <h1 class="banner-title">Solutions</h1>
  </section>

  <main class="card content-card">
    <h2 class="section-heading">INTRODUCTION</h2>
    <div class="intro-copy">
      <p>Our proven solutions help you increase the ROI of your marketing programs and improve productivity of your sales force and channel partners. Talk to us to learn more about how we can help you get results faster and allow you to do more with your budgets.</p>
      <p><strong>Suspendisse vel nisl viverra tellus fermentum.</strong><br>
      Congue sit amet a justo. Donec fringilla, purus a congue suscipit, sapien risus varius ligula, ut volutpat mauris magna vitae eros. Maecenas tincidunt porttitor nisi, vitae sodales leo venenatis sit amet. Curabitur euismod purus quis ipsum dictum vestibulum. Aliquam eu sem eget justo ornare auctor. Morbi dictum faucibus sapien, eu dignis sim nisi dignissim quis. Cras id leo quam. Pellentesque a nulla massa, eget sollicitudin orci. Curabitur nec facilisis libero. Suspendisse congue, metus vitae ullamcorper iaculis, urna magna facilisis mi, id ornare sapien dolor id enim.</p>
      <p><strong>Maecenas in ligula non nisl suscipit scelerisque.</strong><br>
      Donec non odio libero, vulputate fermentum nisl. Vivamus volutpat ante sit amet urna vestibulum non lacinia justo dignissim. Nulla placerat tempus laoreet. Maecenas et faucibus magna. Nulla posuere libero in ante laoreet a posuere magna porta.</p>
    </div>
    <figure class="photo-frame">
      <div class="photo-top" role="img" aria-label="Hand with a pen pointing at printed sales charts beside a laptop"></div>
      <div class="photo-bottom" role="img" aria-label="Smiling businesswoman next to a rising line chart"></div>
    </figure>
  </main>

  <aside class="card links-card">
    <h2 class="section-heading">RELEVANT LINKS <span class="more">&gt;</span></h2>
    <ul class="related-links">
      <li><a href="#">Sales Planning Analytics</a></li>
      <li><a href="#">Sales Productivity Centers</a></li>
      <li><a href="#">Sales measurement Analytics</a></li>
    </ul>
  </aside>

  <footer class="footer">
    <div class="footer-note">© 2008 Corvexa, Inc. | Disclaimer</div>
  </footer>
</body>
</html>
```